VelloTask Business Card

Our company is called VelloTask and we are based in Tel Aviv, Israel. We create innovative and exciting methods for getting people on the web engaged with content. We need a cool yet professional business card that will represent our management level employees. keep in mind this is a start up company with a young atmosphere. You can be inspired by our logo (file attached, make sure you have the right font "Ubuntu-Condensed") Use the colors that are used in the logo and create a colourful and professional business card.

```html
<!DOCTYPE html>
<html lang="en">
<head>
<meta charset="utf-8">
<title>VelloTask Business Card</title>
<link rel="stylesheet" href="https://fonts.googleapis.com/css2?family=Ubuntu+Condensed&family=Ubuntu:ital,wght@0,400;1,400&display=swap">
<style>
  :root {
    --stage: #ecebe8;
    --magenta: #e0196e;
    --royal-blue: #2f74b8;
    --sky-blue: #5cb6e2;
    --ink: #2f3033;
    --violet: #8a2f8f;
    --pale-sky: #e4eff8;
    --pale-sky-light: #eef4fa;
    --white: #ffffff;
  }
  * { box-sizing: border-box; margin: 0; padding: 0; }
  html, body {
    width: 1200px; height: 873px; overflow: hidden;
    background: var(--stage);
  }
  .canvas {
    width: 1200px; height: 873px;
    display: flex; flex-direction: column; align-items: center; justify-content: center;
    gap: 50px;
  }
  .card {
    position: relative;
    width: 620px; height: 354px;
    box-shadow: 0 6px 18px rgba(0,0,0,.12);
  }

  /* ---------- front ---------- */
  .card--front {
    background: var(--magenta);
    padding: 14px;
  }
  .card--front .frame-blue {
    width: 100%; height: 100%;
    background: var(--royal-blue);
    padding: 4px;
  }
  .card--front .frame-white {
    width: 100%; height: 100%;
    background: var(--white);
    padding: 4px;
    clip-path: polygon(18px 0, calc(100% - 18px) 0, 100% 18px, 100% calc(100% - 18px), calc(100% - 18px) 100%, 18px 100%, 0 calc(100% - 18px), 0 18px);
  }
  .card--front .panel {
    position: relative;
    width: 100%; height: 100%;
    clip-path: polygon(16px 0, calc(100% - 16px) 0, 100% 16px, 100% calc(100% - 16px), calc(100% - 16px) 100%, 16px 100%, 0 calc(100% - 16px), 0 16px);
  }
  .pattern-fill {
    position: absolute; inset: 0;
    background: linear-gradient(135deg, var(--pale-sky), var(--pale-sky-light));
  }
  .brand {
    position: absolute; inset: 0;
    display: flex; align-items: center; justify-content: center; gap: 18px;
  }
  .brand-dot {
    width: 70px; height: 70px; border-radius: 50%;
    background: var(--magenta);
  }
  .brand-name {
    font-family: "Ubuntu Condensed", "Ubuntu", sans-serif;
    font-size: 74px; line-height: 1; color: var(--ink);
  }

  /* ---------- back ---------- */
  .card--back {
    background: var(--sky-blue);
    padding: 10px;
  }
  .card--back .panel {
    position: relative;
    width: 100%; height: 100%;
    background: var(--white);
    clip-path: polygon(14px 0, calc(100% - 14px) 0, 100% 14px, 100% calc(100% - 14px), calc(100% - 14px) 100%, 14px 100%, 0 calc(100% - 14px), 0 14px);
  }
  .pattern-band {
    position: absolute; left: 0; right: 0; bottom: 0; height: 124px;
    background: linear-gradient(180deg, var(--pale-sky-light), var(--pale-sky));
  }
  .contact {
    position: absolute; left: 34px; top: 24px;
    font-family: "Ubuntu", sans-serif;
  }
  .person-name {
    font-family: "Ubuntu Condensed", "Ubuntu", sans-serif;
    font-size: 30px; color: var(--magenta); line-height: 1.1;
  }
  .person-title {
    font-size: 13px; font-style: italic; color: var(--magenta);
    line-height: 16px; margin-bottom: 10px;
  }
  .contact-list { list-style: none; }
  .contact-list li {
    display: flex; align-items: center; gap: 8px;
    font-size: 13px; color: var(--ink); line-height: 19px;
  }
  .contact-list svg { width: 13px; height: 13px; flex: none; fill: var(--violet); }
</style>
</head>
<body>
<main class="canvas">

  <section class="card card--front" aria-label="Business card front">
    <div class="frame-blue">
      <div class="frame-white">
        <div class="panel">
          <div class="pattern-fill" role="img" aria-label="Soft pastel dotted background pattern"></div>
          <div class="brand">
            <span class="brand-dot"></span>
            <span class="brand-name">VelloTask</span>
          </div>
        </div>
      </div>
    </div>
  </section>

  <section class="card card--back" aria-label="Business card back">
    <div class="panel">
      <div class="pattern-band" role="img" aria-label="Soft pastel dotted band"></div>
      <div class="contact">
        <p class="person-name">FirstName Surname</p>
        <p class="person-title">Title/Position</p>
        <ul class="contact-list">
          <li><svg viewBox="0 0 12 12"><path d="M6 0a4 4 0 0 0-4 4c0 3 4 8 4 8s4-5 4-8a4 4 0 0 0-4-4zm0 5.5A1.5 1.5 0 1 1 6 2.5a1.5 1.5 0 0 1 0 3z"/></svg>14 Lilac Row, Dune Park, TA 6124</li>
          <li><svg viewBox="0 0 12 12"><path d="M0 2h12v8H0z M0 2l6 4 6-4" stroke="#fff" stroke-width="1"/></svg>hello@vellotask.com</li>
          <li><svg viewBox="0 0 12 12"><path d="M2 0h3l1 3-2 1.5a7 7 0 0 0 3.5 3.5L9 6l3 1v3a2 2 0 0 1-2 2C4.5 12 0 7.5 0 2a2 2 0 0 1 2-2z"/></svg>+972 3 555 0142</li>
          <li><svg viewBox="0 0 12 12"><path d="M1 4h10v7H1z M3 0h6v4H3z"/></svg>+972 3 555 0187</li>
          <li><svg viewBox="0 0 12 12"><path d="M3 0h6a1 1 0 0 1 1 1v10a1 1 0 0 1-1 1H3a1 1 0 0 1-1-1V1a1 1 0 0 1 1-1zm0 2v7h6V2z"/></svg>+972 54 555 016</li>
          <li><svg viewBox="0 0 12 12"><circle cx="6" cy="6" r="6"/><path d="M0 6h12M6 0v12" stroke="#fff" stroke-width="1"/></svg>www.vellotask.com</li>
        </ul>
      </div>
    </div>
  </section>

</main>
</body>
</html>
```